Looking for an Innovative Print Design (Service Directory)

We need a new design for our advertisement within a printed colour services directory.

We are a compensation law firm called Velbrook Compensation Lawyers. Feel free to take a browse of our website www.velbrooklegal.com.au to get an idea of what we do and the kind of firm we are.

We are in the process of redeveloping our website and as such, so please don't adhere to the design principles of the current site- impress us with your originality!

On top of any editable formats, your final submissions must include a .pdf copy.
The same design will need to be presented in two dimensions:

- 154mm x 118mm (B1/B2 Half Page);
- 175mm x 113mm (B4 Half Page).

[For more information refer to attached Pdf.]

We have attached for you a few examples of other firms' designs (Sample1,2,3). These are by no means good, or what we're after, it's just to provide you with an idea of what sort of advertisements go into the service directory.

Hi all,

We want to emphasise that a priority of the design is that it must look:
• Professional
• Sophisticated
Please do not hesitate to use completely different colour schemes to the ones that are on our website- as we have said, our website will change in the near future, so cohesion between the current project and the website is not necessary!

Thanks!

Thank you for your submissions so far. There are some great ideas hidden in there. 

An issue we are having is that most of you are conforming to the same understanding of what it should look like. Remember that there is NO NEED to be bound by the image of firm as is. That is, feel free to use a different colour logo.

For inspiration, we relate well to the design aesthetics of: http://www.tinfernstudio.co.uk/

Look forward to seeing your 'out of the box' submissions. 

Reason: We've received a large amount of fantastic designs. However, what we're really looking for is something original. Please feel free to think outside the box (the final design doesn't need to look like a print ad), and construct a design that is completely incongruous with our website! While we do appreciate a minimalistic design, we have yet to receive something that really grabs your attention with its visuals. We're not sure but this may or may not be achieved with a full colour design. Thanks for all your submissions- they all have some features that really click with us. We look forward to the next wave of submissions!

Target Market(s)

We have various target markets, including mainly families, elderly people, blue collar workers.

These are individuals who are looking for assistance. They feel helpless or wronged.

Keep in mind that the people accessing these are those who prefer going to a printed directory rather than using a google search.

Industry/Entity Type

Law Firm

Font styles to use
Serif
Sans Serif

Requirements
Must have
• - Our name 'Velbrook Compensation Lawyers'
- Our logo (attached as logo.eps, logo.png, and logo.tif)
- Must include phone number as 1300 XXX XXX (this must be prominent)
- Must include the following service areas in these words: Motor vehicle claims, medical claims, superannuation claims, Workplace claims, negligence claims
- Our email address: info@velbrooklegal.com.au
- Our website address: www.velbrooklegal.com.au
- The following catchphrases: '98% success rate', and 'No win no fee' in those words
- Our location '412 Carvel Lane, Smithville, SYDNEY'
- For sizing dimensions, we need one in 154mm x 118mm and also a design in 175mm x 113mm (B4 Half Page) [refer to pdf attached]
Nice to have
• - Text indicating free initial consulatation
- Professional colour scheme
- As our website will be changed, do not worry about making the advertisement cohesive with our website design
- We want the design to be modern, but still professional
- Clean typeface
- No gradient colour scheme
- When designing, if you are looking to place more text onto the advertisement, these may be some considerations (feel free to change the wording): Accredited specialists, home and hospital visits

```html
<!DOCTYPE html>
<html lang="en">
<head>
<meta charset="utf-8">
<title>Velbrook Compensation Lawyers – Directory Advertisement</title>
<link href="https://fonts.googleapis.com/css2?family=Questrial&family=Open+Sans:wght@700&display=swap" rel="stylesheet">
<style>
  :root {
    --navy: #34356e;
    --teal: #17a89d;
    --teal-text: #1fa59b;
    --white: #ffffff;
    --page: #e6e6e6;
    --photo-a: #b9bcc4;
    --photo-b: #5a5e6e;
  }
  * { box-sizing: border-box; margin: 0; padding: 0; }
  html, body {
    width: 1200px; height: 900px; overflow: hidden;
    background: var(--page);
  }
  .ad {
    position: absolute; left: 84px; top: 57px;
    width: 1034px; height: 667px;
    background: var(--white);
    font-family: "Questrial", "Century Gothic", sans-serif;
    overflow: hidden;
  }
  .header {
    position: absolute; left: 0; top: 0; width: 1034px; height: 172px;
    background: var(--navy);
  }
  .brand-mark {
    position: absolute; left: 52px; top: 54px;
    width: 86px; height: 86px; border-radius: 50%;
    background: var(--teal);
  }
  .brand-name {
    position: absolute; left: 154px; top: 50px;
    font-size: 44px; font-weight: 400; line-height: 1; color: var(--white);
    white-space: nowrap; letter-spacing: 0;
  }
  .tagline {
    position: absolute; left: 156px; top: 105px;
    font-size: 36px; line-height: 1; color: var(--teal-text);
    letter-spacing: 6.2px; white-space: nowrap;
  }
  .photo {
    position: absolute; left: 0; top: 174px; width: 500px; height: 391px;
    background: linear-gradient(160deg, var(--photo-a) 0%, #8d909c 45%, var(--photo-b) 100%);
  }
  .benefits {
    position: absolute; left: 500px; top: 174px; width: 534px; height: 391px;
    background: var(--teal);
  }
  .promises {
    position: absolute; top: 38px; left: 0; width: 534px;
    color: var(--white); font-size: 25px; line-height: 26px;
  }
  .promises .left {
    position: absolute; right: 298px; text-align: right; white-space: nowrap;
  }
  .promises .divider {
    position: absolute; left: 248px; top: 4px; width: 2px; height: 46px;
    background: var(--navy);
  }
  .promises .right {
    position: absolute; left: 261px; white-space: nowrap;
  }
  .benefit-list {
    position: absolute; left: 32px; top: 110px; list-style: none;
    font-family: "Open Sans", Arial, sans-serif; font-weight: 700;
    font-size: 28px; line-height: 40px; color: var(--navy);
    letter-spacing: -0.2px;
  }
  .benefit-list li { display: flex; align-items: center; white-space: nowrap; }
  .benefit-list li::before {
    content: ""; width: 16px; height: 16px; background: var(--white);
    margin-right: 10px; flex: none;
  }
  .service-areas {
    position: absolute; left: 32px; right: 24px; top: 354px;
    font-size: 14px; line-height: 17px; color: var(--white);
  }
  .footer {
    position: absolute; left: 0; top: 567px; width: 1034px; height: 100px;
    background: var(--navy); color: var(--white);
  }
  .contact {
    position: absolute; left: 32px; top: 16px;
    font-size: 21px; line-height: 23px; letter-spacing: 3.4px;
    font-style: normal; white-space: nowrap;
  }
  .phone {
    position: absolute; left: 524px; top: 10px;
    font-size: 76px; line-height: 1; letter-spacing: 1px; white-space: nowrap;
  }
</style>
</head>
<body>
  <main class="ad">
    <header class="header">
      <span class="brand-mark" aria-hidden="true"></span>
      <h1 class="brand-name">VELBROOK COMPENSATION LAWYERS</h1>
      <p class="tagline">We are specialists in compensation</p>
    </header>

    <div class="photo" role="img" aria-label="Photograph of two business people shaking hands in front of a group of smiling office staff"></div>

    <section class="benefits">
      <div class="promises">
        <p class="left">98% success rate<br>No win No fee</p>
        <span class="divider" aria-hidden="true"></span>
        <p class="right">your first<br>consultation is free</p>
      </div>
      <ul class="benefit-list">
        <li>Expert support</li>
        <li>Free advice</li>
        <li>If we don't win, you don't pay</li>
        <li>Maximising your claim</li>
        <li>We speak your language</li>
        <li>An office near you</li>
      </ul>
      <p class="service-areas">Motor vehicle claims, medical claims, superannuation claims,<br>Workplace claims, negligence claims</p>
    </section>

    <footer class="footer">
      <address class="contact">
        412 Carvel Lane, Smithville, SYDNEY<br>
        info@velbrooklegal.com.au<br>
        www.velbrooklegal.com.au
      </address>
      <p class="phone">1300 482 390</p>
    </footer>
  </main>
</body>
</html>
```